Dalton Power Supply, Inc. Business Card Design

We are an Electrical Distributor looking for a Modern, Professional Business Card design.

Target Market(s)

Residential Commercial Industrial

Industry/Entity Type

Electrical

Contact Information for Business Card

Dalton Power Supply, Inc.
418 Maple Ridge Lane
Brookvale, NC 27514
555-214-7630
555-214-8842 Fax
daltonpower@brightmail-example.net

```html
<!DOCTYPE html>
<html lang="en">
<head>
<meta charset="utf-8">
<title>Dalton Power Supply, Inc. – Business Card</title>
<link rel="stylesheet" href="https://fonts.googleapis.com/css2?family=Open+Sans:wght@400;600&display=swap">
<style>
  :root {
    --red: #d8232a;
    --charcoal: #4a4a4a;
    --text: #333333;
    --card: #ffffff;
    --backdrop: #e8e5e1;
    --ghost: #f2f2f2;
  }
  html, body {
    margin: 0;
    width: 1200px;
    height: 1000px;
    overflow: hidden;
    background: var(--backdrop);
    font-family: "Open Sans", Arial, sans-serif;
  }
  .card {
    position: absolute;
    left: 265px;
    width: 665px;
    height: 397px;
    background: var(--card);
    border-radius: 22px;
    overflow: hidden;
    box-shadow: 0 4px 14px rgba(0,0,0,0.18);
  }
  .card--front { top: 73px; }
  .card--back { top: 533px; }

  .ghost-ring {
    position: absolute;
    left: 356px; top: 27px;
    width: 302px; height: 302px;
    border: 6px solid var(--ghost);
    border-radius: 50%;
    box-sizing: border-box;
  }

  .brand-ring {
    position: absolute;
    border: 5px solid var(--charcoal);
    border-radius: 50%;
    box-sizing: border-box;
  }
  .brand-name {
    position: absolute;
    margin: 0;
    color: var(--red);
    font-weight: 600;
    line-height: 1.08;
    letter-spacing: 0.3px;
    white-space: nowrap;
  }
  .card--front .brand-ring { left: 36px; top: 33px; width: 110px; height: 110px; }
  .card--front .brand-name { left: 160px; top: 62px; font-size: 23px; }

  .holder { position: absolute; left: 33px; top: 202px; }
  .holder-name { margin: 0; color: var(--red); font-size: 22px; font-weight: 600; line-height: 30px; }
  .holder-role { margin: 0; color: var(--text); font-size: 16px; line-height: 22px; }

  .divider {
    position: absolute;
    left: 33px; right: 32px; top: 259px;
    height: 1px;
    background: var(--charcoal);
  }

  .contact-list {
    position: absolute;
    left: 33px; top: 276px;
    margin: 0; padding: 0;
    list-style: none;
    font-size: 16px;
    color: var(--text);
  }
  .contact-list li { display: flex; align-items: center; height: 23.5px; }
  .contact-list svg { width: 14px; height: 14px; margin-right: 8px; fill: var(--red); }

  .address {
    position: absolute;
    right: 32px; top: 276px;
    margin: 0;
    text-align: right;
    font-style: normal;
    font-size: 16px;
    line-height: 23.5px;
    color: var(--text);
  }
  .address-company { color: var(--red); font-weight: 600; }

  .band { position: absolute; bottom: 0; height: 30px; }
  .band--charcoal { left: 0; width: 353px; background: var(--charcoal); }
  .band--red { left: 360px; right: 0; background: var(--red); }

  .card--back .brand-ring { left: 112px; top: 120px; width: 154px; height: 154px; border-width: 6px; }
  .card--back .brand-name { left: 286px; top: 160px; font-size: 34px; }
</style>
</head>
<body>

<section class="card card--front" aria-label="Business card front">
  <div class="ghost-ring"></div>
  <div class="brand-ring"></div>
  <h1 class="brand-name">DALTON POWER<br>SUPPLY, INC</h1>

  <div class="holder">
    <p class="holder-name">Dalton Reeves</p>
    <p class="holder-role">Owner / Founder</p>
  </div>

  <div class="divider"></div>

  <ul class="contact-list">
    <li>
      <svg viewBox="0 0 16 16" aria-hidden="true"><path d="M1 5c0-2 3-3 7-3s7 1 7 3v1h-4V4.5H5V6H1zM3 7h10l1 7H2zM8 9a2 2 0 1 0 0 4 2 2 0 0 0 0-4z"/></svg>
      555-214-7630
    </li>
    <li>
      <svg viewBox="0 0 16 16" aria-hidden="true"><path d="M4 1h8v4H4zM1 6h14v6h-3v-2H4v2H1zM5 11h6v4H5z"/></svg>
      555-214-8842
    </li>
    <li>
      <svg viewBox="0 0 16 16" aria-hidden="true"><path d="M1 3h14v1L8 9 1 4zM1 5.5l7 5 7-5V13H1z"/></svg>
      daltonpower@brightmail-example.net
    </li>
  </ul>

  <address class="address">
    <span class="address-company">Dalton Power Supply, Inc.</span><br>
    418 Maple Ridge Lane<br>
    Brookvale, NC 27514
  </address>

  <div class="band band--charcoal"></div>
  <div class="band band--red"></div>
</section>

<section class="card card--back" aria-label="Business card back">
  <div class="brand-ring"></div>
  <h2 class="brand-name">DALTON POWER<br>SUPPLY, INC</h2>
</section>

</body>
</html>
```